Start-up Cleaning Business Needs Professional Business Cards

Marta's Butler Cleaning, LLC, is a start-up business based in the Northern Virginia suburbs of Washington, DC. MBC provides cleaning and housekeeping services for homes and offices. We have three core values:

1. We are personal. We value knowing and being known by our customers and each other. If you want nameless, faceless service, you should choose another provider. We put "personal" at the front of the list, because it is most important to us; the design we choose will convey this value.

2. Like a hotel concierge, we are professional in attitude, posture, communication and processes.

3. Like a hotel concierge, we solve problems with a can-do attitude and never make excuses.

Our uniforms are khaki pants with pink polo shirts.

Our logo is attached. There are other symbols, not represented in our logo, that may convey our values well, such as a top hat and bow tie, magnifying glass, desk bell, etc.

Please include fields for an individual's name and title, office phone number, mobile phone number, email address and website address (www.martasbutlercleaning.example).

Standard U.S. size: 2" x 3.5"
Updates

I should have mentioned that the purpose of all our advertising - business cards included - is to motivate potential customers to call or email to arrange a free in-home estimate.

```html
<!DOCTYPE html>
<html lang="en">
<head>
<meta charset="utf-8">
<title>Marta's Butler Cleaning — Business Cards</title>
<link rel="stylesheet" href="https://fonts.googleapis.com/css2?family=Quicksand:wght@400;500&family=Ubuntu:wght@400;500&display=swap">
<style>
  :root {
    --backdrop: #e9e6e8;
    --card: #fde9f1;
    --ink: #3c3a3c;
    --ink-soft: #6d6a6d;
    --pink: #ea1f83;
    --pink-soft: #f4b3d1;
    --sketch: #d7c6cd;
  }
  * { box-sizing: border-box; margin: 0; padding: 0; }
  html, body {
    width: 1200px;
    height: 941px;
    overflow: hidden;
    background: var(--backdrop);
  }
  .stage {
    position: relative;
    width: 1200px;
    height: 941px;
  }
  .card {
    position: absolute;
    top: 120px;
    width: 400px;
    height: 700px;
    background: var(--card);
    box-shadow: 0 10px 28px rgba(0,0,0,0.18);
    overflow: hidden;
  }
  .card--front { left: 170px; }
  .card--back  { left: 630px; border-bottom: 8px solid var(--pink); }

  .illustration {
    position: absolute;
    border-radius: 30px;
  }
  .card--front .illustration {
    left: 40px; top: 40px; width: 320px; height: 440px;
    background: linear-gradient(160deg, #f7c9dc 0%, #efa8c7 55%, #e9d9df 100%);
  }
  .card--back .illustration {
    left: 70px; top: 180px; width: 200px; height: 440px;
    background: linear-gradient(180deg, #f3dce5 0%, #ecd3dc 100%);
    opacity: 0.8;
  }

  .wordmark {
    font-family: "Quicksand", sans-serif;
    font-weight: 400;
    color: var(--ink);
    line-height: 1.1;
  }
  .card--front .wordmark {
    position: absolute;
    left: 40px; top: 520px; width: 320px;
    font-size: 38px;
  }
  .card--back .wordmark {
    position: absolute;
    left: 40px; top: 70px; width: 320px;
    font-size: 32px;
  }

  .contact {
    position: absolute;
    right: 30px; bottom: 40px;
    text-align: right;
    font-family: "Ubuntu", sans-serif;
    color: var(--ink);
  }
  .contact__name {
    font-size: 38px;
    font-weight: 500;
    color: var(--pink);
    line-height: 1;
  }
  .contact__title {
    font-size: 15px;
    color: var(--ink-soft);
    margin-bottom: 22px;
  }
  .contact__line {
    font-size: 14px;
    line-height: 1.75;
  }
  .contact__line b { font-weight: 500; }
</style>
</head>
<body>
<main class="stage">
  <section class="card card--front">
    <div class="illustration" role="img" aria-label="Sketched illustration of a housekeeper in a pink uniform mopping the floor"></div>
    <p class="wordmark">Marta's Butler Cleaning</p>
  </section>

  <section class="card card--back">
    <p class="wordmark">Marta's Butler Cleaning</p>
    <div class="illustration" role="img" aria-label="Faint sketched illustration of a housekeeper holding a mop"></div>
    <div class="contact">
      <p class="contact__name">john doe</p>
      <p class="contact__title">product manager</p>
      <p class="contact__line"><b>mobile:</b> 0123456789</p>
      <p class="contact__line"><b>office phone:</b> 055-123-4567</p>
      <p class="contact__line"><b>web:</b> www.martasbutlercleaning.example</p>
      <p class="contact__line"><b>email:</b> john@martasbutlercleaning.example</p>
    </div>
  </section>
</main>
</body>
</html>
```